Wedding Invitations

We are a printing company "inkmorrow" and require multiple wedding invitation designs for our customers in store and online. We would like the designs to be editable in Photoshop if possible, if not then a layout with suggested fonts would be the next best option. We are open to suggestions on design but would like to stick to the general wedding themes some with a modern and some with a classical feel

Industry/Entity Type

Printing

```html
<!DOCTYPE html>
<html lang="en">
<head>
<meta charset="utf-8">
<title>Wedding Invitation</title>
<link rel="stylesheet" href="https://fonts.googleapis.com/css2?family=Pinyon+Script&family=Libre+Caslon+Text&display=swap">
<style>
  :root {
    --mint: #b4ddd0;
    --mint-deep: #9fd3c4;
    --crimson: #d0245a;
    --ink-brown: #7b6a56;
    --bench-brown: #8a6a55;
    --serif: "Libre Caslon Text", Georgia, serif;
    --script: "Pinyon Script", cursive;
  }
  html, body {
    margin: 0;
    padding: 0;
    overflow: hidden;
    background: var(--mint);
  }
  .invitation {
    position: relative;
    width: 1200px;
    height: 848px;
    background: var(--mint);
    overflow: hidden;
    color: var(--ink-brown);
    font-family: var(--serif);
  }
  .star-canopy {
    position: absolute;
    left: 0; top: 0;
    width: 1200px; height: 220px;
    background: linear-gradient(180deg, var(--mint-deep) 0%, rgba(159,211,196,0.5) 55%, rgba(180,221,208,0) 100%);
  }
  .bird-mark {
    position: absolute;
    left: 266px; top: 41px;
    width: 86px; height: 52px;
    background: rgba(208,36,90,0.35);
    border-radius: 6px;
  }
  .couple-on-bench {
    position: absolute;
    left: 34px; top: 427px;
    width: 450px; height: 396px;
    background: linear-gradient(180deg, #c9a98a 0%, #8a6a55 100%);
    border-radius: 12px;
  }
  .line {
    position: absolute;
    margin: 0;
    white-space: nowrap;
    text-transform: uppercase;
    font-size: 20px;
    line-height: 1;
    letter-spacing: 0.2px;
  }
  .names {
    position: absolute;
    margin: 0;
    font-family: var(--script);
    font-weight: 400;
    color: var(--crimson);
    font-size: 72px;
    line-height: 1;
    white-space: nowrap;
  }
  .ampersand {
    position: absolute;
    left: 612px; top: 176px;
    margin: 0;
    font-family: var(--serif);
    font-size: 44px;
    line-height: 1;
    color: var(--ink-brown);
  }
  .rsvp {
    position: absolute;
    right: 39px; top: 708px;
    margin: 0;
    text-align: right;
    font-size: 16px;
    line-height: 22px;
  }
</style>
</head>
<body>
<main class="invitation">
  <div class="star-canopy" role="img" aria-label="Soft pattern of pale stars across the top edge"></div>
  <div class="bird-mark" role="img" aria-label="Small pair of flying birds"></div>
  <div class="couple-on-bench" role="img" aria-label="Illustration of a couple seen from behind, sitting on a park bench"></div>

  <p class="line" style="left:556px; top:88px;">Togther with their families</p>

  <h1 class="names" style="left:462px; top:118px;">Bride</h1>
  <p class="ampersand">&amp;</p>
  <h1 class="names" style="left:598px; top:228px;">Bride groom</h1>

  <p class="line" style="left:555px; top:330px;">Invite you to share in their</p>
  <p class="line" style="left:556px; top:372px;">Wedding celebration</p>

  <p class="line" style="left:555px; top:458px;">Saturday,the twenty-second of December</p>
  <p class="line" style="left:556px; top:497px;">Two thousand and fourteen</p>
  <p class="line" style="left:556px; top:540px;">Two o’clock the afthernoon</p>

  <p class="line" style="left:557px; top:612px;">Anywhere hotel</p>
  <p class="line" style="left:556px; top:645px;">City, State</p>

  <p class="rsvp">RSVP<br>by date<br>phone number</p>
</main>
</body>
</html>
```